Make attractive Packaging label for NUT BUTTERS jars

We at Velvet Orchard are launching our own line of NUT BUTTERS. We will be serving them in GLASS JARS ready packaged. I need attractive luxurious design for glass jar and should be designed ready to print.
I have attached glass jar pictures and measurement sheet.
My company logo has been attached. Also company details can be found on our facebook page.
product will be

ALMOND BUTTER
CASHEW BUTTER
PEANUT BUTTER
HAZELNUT BUTTER.

```html
<!DOCTYPE html>
<html lang="en">
<head>
<meta charset="utf-8">
<title>Velvet Orchard – Almond Butter Jar Label</title>
<link rel="stylesheet" href="https://fonts.googleapis.com/css2?family=Rye&family=Roboto+Condensed:wght@700&display=swap">
<style>
  :root {
    --backdrop: #3b3b3b;
    --label-white: #ffffff;
    --pattern-tint: #f1f1f1;
    --cocoa: #5a2d12;
    --cocoa-dark: #4a220c;
    --honey: #f2c12e;
    --honey-deep: #e6ad1c;
    --gold: #b8862b;
    --almond-light: #d9a86a;
    --almond-dark: #8a4e24;
    --leaf: #6e9b3a;
  }
  * { margin: 0; padding: 0; box-sizing: border-box; }
  html, body { width: 1200px; height: 612px; overflow: hidden; }
  body { background: var(--backdrop); position: relative; font-family: "Roboto Condensed", sans-serif; font-weight: 700; }

  .jar-label {
    position: absolute; left: 100px; top: 36px;
    width: 1000px; height: 540px;
    background: var(--label-white);
    overflow: hidden;
  }
  .label-rule-top {
    position: absolute; left: 0; top: 0; width: 100%; height: 10px;
    border-top: 4px solid var(--cocoa); border-bottom: 2px solid var(--cocoa);
  }
  .label-notch { position: absolute; left: 488px; top: 10px; }

  .pattern-field {
    position: absolute; left: 0; top: 12px; width: 100%; height: 318px;
    background: radial-gradient(ellipse at center, var(--label-white) 40%, var(--pattern-tint) 100%);
  }

  .brand-name {
    position: absolute; right: 40px; top: 40px;
    font-family: "Rye", serif; font-weight: 400; font-size: 30px; line-height: 1;
    color: var(--gold); text-align: center;
  }

  .product-title {
    position: absolute; left: 0; top: 66px; width: 100%;
    text-align: center;
    font-family: "Rye", serif; font-weight: 400;
    color: var(--cocoa); font-size: 80px; line-height: 1.05; letter-spacing: 4px;
  }

  .certification-column {
    position: absolute; left: 70px; top: 150px;
    width: 92px; height: 262px;
    background: var(--honey);
    border: 3px solid var(--cocoa);
    border-radius: 46px 46px 6px 6px;
    display: flex; flex-direction: column; align-items: center;
    padding-top: 18px; gap: 10px; z-index: 3;
  }
  .cert-badge {
    width: 56px; height: 56px; border-radius: 50%;
    background: var(--honey-deep); border: 2px solid var(--cocoa);
  }
  .cert-badge.square { border-radius: 4px; width: 60px; height: 42px; background: var(--leaf); border-color: var(--leaf); }

  .almond-illustration {
    position: absolute; left: 370px; top: 262px; width: 260px; height: 128px;
    border-radius: 50%;
    background: radial-gradient(ellipse at 50% 55%, var(--almond-light) 0%, var(--almond-dark) 70%, rgba(138,78,36,0) 72%);
    z-index: 2;
  }

  .flavour-band {
    position: absolute; left: 0; top: 330px; width: 100%; height: 70px;
    background: var(--honey);
  }
  .texture-name {
    position: absolute; left: 176px; top: 358px;
    font-size: 30px; line-height: 1; color: var(--cocoa-dark); letter-spacing: .5px; z-index: 3;
  }
  .natural-claim {
    position: absolute; right: 110px; top: 366px;
    font-size: 22px; line-height: 1; color: var(--cocoa-dark); z-index: 3;
  }

  .benefit-band {
    position: absolute; left: 0; top: 400px; width: 100%; height: 44px;
    background: var(--cocoa);
    border-top: 3px solid var(--cocoa-dark);
    border-bottom: 3px solid var(--cocoa-dark);
    display: flex; align-items: center; justify-content: space-between;
    padding: 0 120px 0 176px;
    color: var(--label-white); font-size: 23px; letter-spacing: .5px;
  }
  .benefit-band .figure { font-size: 30px; }

  .weight-band {
    position: absolute; left: 0; top: 444px; width: 100%; height: 64px;
    background: var(--honey);
    display: flex; align-items: center; justify-content: center;
    font-size: 25px; color: var(--cocoa-dark); letter-spacing: .5px;
  }
  .label-rule-bottom {
    position: absolute; left: 0; top: 508px; width: 100%; height: 12px;
    border-top: 3px solid var(--cocoa); border-bottom: 2px solid var(--cocoa);
    background: var(--label-white);
  }
</style>
</head>
<body>
  <main class="jar-label">
    <div class="label-rule-top"></div>
    <svg class="label-notch" width="24" height="14" viewBox="0 0 24 14" aria-hidden="true">
      <polygon points="0,0 24,0 12,12" fill="#5a2d12"/>
    </svg>

    <div class="pattern-field" role="img" aria-label="Faint grey outline pattern of scattered almonds"></div>

    <p class="brand-name">Velvet Orchard</p>

    <h1 class="product-title">ALMOND<br>BUTTER</h1>

    <aside class="certification-column" aria-label="Certification badges">
      <span class="cert-badge"></span>
      <span class="cert-badge"></span>
      <span class="cert-badge"></span>
      <span class="cert-badge square"></span>
    </aside>

    <section class="flavour-band"></section>
    <div class="almond-illustration" role="img" aria-label="Illustration of whole and shelled almonds with green leaves"></div>
    <p class="texture-name">SMOOTH</p>
    <p class="natural-claim">ALL NATURAL</p>

    <section class="benefit-band">
      <span>RICH SOURCE OF VITAMIN E</span>
      <span>HIGH IN PROTEIN <span class="figure">21%</span></span>
    </section>

    <section class="weight-band">NET WT. 12 OZ (340g)</section>
    <div class="label-rule-bottom"></div>
  </main>
</body>
</html>
```